Lantern - Web Design Project

We are seeking to have our website redesigned. Our current webpage is rather dated looking www.lantern-outcomes.com We will be utilizing similar content to explain our services as what is in the website now. We do not see it at a retail portal but rather a website for those inquiring about our services as a reference check so to speak.

We wish to have a look that is considered clean, fresh, contemporary and contains a business savvy vibe.

We prefer isolated white background and also wish to retain the integrity of our Logo and colour scheme.

We are looking for something that doesnt look like it was designed at home on sitemoose. We are hoping to find something that looks like it would reside on a tablet.
Updates

Hello designers!

We apologize for our tardiness as we have been quite preoccupied. We will be extending our invites to the end of January!

Hello All,

Please review our offer once again for updated requirements.  We are hoping to accept a design by months end.

Lantern

Target Market(s)

Business to business clients and Large manufacturers

Industry/Entity Type

Retail

Requirements
Must have
• Existing Logo

There must be an area dedicated to an intro video that will be incorporated on our landing page.

We require design of the other pages as well not only the landing page.

```html
<!DOCTYPE html>
<html lang="en">
<head>
<meta charset="utf-8">
<title>Lantern – Performance Solutions</title>
<link href="https://fonts.googleapis.com/css2?family=Open+Sans:wght@400;500;600&display=swap" rel="stylesheet">
<style>
:root{
  --page:#ffffff;
  --rail:#9aa39f;
  --rail-dark:#8d9692;
  --ink:#333a3a;
  --accent:#9b0a0a;
  --muted:#7a7a7a;
  --rule:#dddddd;
  --card-top:#666666;
  --card-bottom:#9a9a9a;
  --card-face:#f7f7f7;
  --button:#1a1a1a;
}
*{box-sizing:border-box;margin:0;padding:0}
html,body{width:1200px;height:900px;overflow:hidden;background:var(--page)}
body{position:relative;font-family:Arial,Helvetica,sans-serif;color:var(--ink)}
.rail{position:absolute;top:0;height:900px;background:linear-gradient(90deg,var(--rail-dark),var(--rail),var(--rail-dark))}
.rail-left{left:40px;width:68px}
.rail-right{left:1108px;width:56px}
.sheet{position:absolute;left:108px;top:0;width:1000px;height:900px;background:var(--page)}
.heading{font-family:"Open Sans",Arial,sans-serif;font-weight:400;color:var(--ink)}
.heading em{font-style:normal;color:var(--accent)}

.feature{position:absolute;top:18px;width:230px;text-align:center}
.feature svg{display:block;margin:0 auto;height:52px}
.feature h3{font-size:20px;line-height:27px;margin-top:23px}
.feature p{font-size:12.5px;line-height:15px;color:var(--muted);margin:18px auto 0;width:210px}

.section-title{position:absolute;left:0;width:1000px;text-align:center;line-height:28px}
.section-title::before{content:"";position:absolute;left:0;right:0;top:50%;border-top:1px solid var(--rule)}
.section-title span{position:relative;background:var(--page);padding:0 10px;font-size:20px}

.card{position:absolute;top:277px;width:308px;background:linear-gradient(#fff,var(--card-face));border-top:15px solid var(--card-top);border-bottom:5px solid var(--card-bottom);border-left:1px dashed #aaa;border-right:1px dashed #aaa;box-shadow:0 3px 4px rgba(0,0,0,.18);text-align:center}
.card .photo{height:180px;width:290px;margin-top:15px}
.card h4{position:relative;font-family:"Open Sans",Arial,sans-serif;font-weight:500;font-size:17px;line-height:24px;color:var(--ink);margin:41px auto 0;width:240px}
.card h4 svg{position:absolute;left:0;top:-14px}
.card p{font-size:12.5px;line-height:15px;color:#444;width:268px;margin:6px auto 0}
.btn{display:inline-block;margin:12px 0 22px;width:109px;height:34px;line-height:32px;border-radius:4px;background:linear-gradient(#3a3a3a,var(--button));color:#fff;font-family:"Open Sans",Arial,sans-serif;font-size:13px;text-decoration:none;border:1px solid #000}

.client{position:absolute;top:822px;height:46px;display:flex;align-items:center;gap:8px;font-family:"Open Sans",Arial,sans-serif;font-weight:600;font-size:20px;color:#444}
.client i{display:block;width:18px;height:18px;background:var(--accent)}
</style>
</head>
<body>
<div class="rail rail-left"></div>
<div class="rail rail-right"></div>

<main class="sheet">
  <section class="features">
    <div class="feature" style="left:20px">
      <svg viewBox="0 0 52 52"><circle cx="26" cy="26" r="24" fill="none" stroke="#222" stroke-width="2"/><path d="M14 12c6 0 10 3 9 8s-6 5-5 10 4 6 2 12c-6-3-12-10-12-18 0-5 2-9 6-12zM32 6c4 2 2 6 6 7s8 4 7 10-6 4-8 9-2 10-6 12c0-6-2-9-5-12s0-7 3-9-2-6 0-10 2-6 3-7z" fill="#222"/></svg>
      <h3 class="heading">Talent <em>Management</em></h3>
      <p>This template has a responsive design, which means you can rezise the browser to any size, and the layout will change. Try it out on your Pocketphone or Slatepad!</p>
    </div>
    <div class="feature" style="left:263px">
      <svg viewBox="0 0 52 52"><rect x="10" y="11" width="32" height="22" rx="2" fill="none" stroke="#222" stroke-width="2.5"/><path d="M20 38h12" stroke="#222" stroke-width="2.5"/><rect x="34" y="22" width="13" height="20" rx="2" fill="#fff" stroke="#222" stroke-width="2.5"/><rect x="5" y="26" width="8" height="15" rx="1.5" fill="#fff" stroke="#222" stroke-width="2.5"/></svg>
      <h3 class="heading">Creating <em>Sales<br>Culture</em></h3>
      <p>This Template is built with TIDY CSS, which allows you to change the site using a few variables(like colors and font-size).</p>
    </div>
    <div class="feature" style="left:506px">
      <svg viewBox="0 0 52 52"><g fill="#222"><circle cx="20" cy="20" r="11"/><g stroke="#222" stroke-width="6"><path d="M20 4v32M4 20h32M9 9l22 22M31 9 9 31"/></g><circle cx="38" cy="36" r="7"/><g stroke="#222" stroke-width="4"><path d="M38 26v20M28 36h20M31 29l14 14M45 29 31 43"/></g></g><circle cx="20" cy="20" r="4" fill="#fff"/><circle cx="38" cy="36" r="2.5" fill="#fff"/></svg>
      <h3 class="heading">Creating <em>Customer<br>Loyalty</em></h3>
      <p>This Template is built with TIDY CSS, which allows you to change the site using a few variables(like colors and font-size).</p>
    </div>
    <div class="feature" style="left:750px">
      <svg viewBox="0 0 52 52"><g fill="#222"><path d="M26 10c6 6 6 16 0 24-6-8-6-18 0-24z"/><path d="M24 36C16 36 9 31 6 23c9 0 16 5 18 13z"/><path d="M28 36c8 0 15-5 18-13-9 0-16 5-18 13z"/><path d="M24 40c-6 4-14 3-19-2 7-3 14-2 19 2zM28 40c6 4 14 3 19-2-7-3-14-2-19 2z"/></g></svg>
      <h3 class="heading">Product <em>Launches</em></h3>
      <p>We love all our Marketstall customers, and with a premium template comes premium support.</p>
    </div>
  </section>

  <h2 class="section-title heading" style="top:240px"><span>Our <em>Performance Solutions</em></span></h2>

  <article class="card" style="left:0">
    <div class="photo" role="img" aria-label="Photo of a team meeting around a conference table" style="background:linear-gradient(135deg,#6b5a4c,#c9c4bc 55%,#8d8f93)"></div>
    <h4 style="padding-left:38px"><svg width="34" height="30" viewBox="0 0 34 30" style="left:0"><g fill="none" stroke="#aaa" stroke-width="2"><circle cx="17" cy="8" r="6"/><circle cx="9" cy="18" r="6"/><circle cx="25" cy="18" r="6"/><path d="M17 14v14"/></g></svg>Business Diagnostics</h4>
    <p>Lorsem hac habitasse platea dictumst. Aliquam in est leo. Aliquam ut urna pulvinar ipsum ultricies fringilla et sed magna. Duis faucibus lorem at leo.</p>
    <a class="btn" href="#">know more...</a>
  </article>

  <article class="card" style="left:346px">
    <div class="photo" role="img" aria-label="Photo of a presenter drawing a chart on a whiteboard" style="background:linear-gradient(90deg,#eef0f2,#dde1e5 45%,#2c3447 75%,#e9eaec)"></div>
    <h4 style="padding-left:38px"><svg width="30" height="30" viewBox="0 0 30 30" style="left:6px"><g fill="none" stroke="#aaa" stroke-width="2.2"><rect x="3" y="5" width="22" height="22" rx="6"/><path d="M11 20l4-2 12-14-2-2-12 14z"/></g></svg>Executive Coaching</h4>
    <p>Lorsem hac habitasse platea dictumst. Aliquam in est leo. Aliquam ut urna pulvinar ipsum ultricies fringilla et sed magna. Duis faucibus lorem at eros.</p>
    <a class="btn" href="#">know more...</a>
  </article>

  <article class="card" style="left:692px">
    <div class="photo" role="img" aria-label="Photo of an audience seated at a business seminar" style="background:linear-gradient(90deg,#8a2a12,#d05a20 35%,#3a2a2a 60%,#cfc8c2)"></div>
    <h4 style="padding-left:42px"><svg width="32" height="32" viewBox="0 0 32 32" style="left:28px"><g fill="none" stroke="#aaa" stroke-width="2"><circle cx="16" cy="9" r="6"/><path d="M4 29c0-8 5-12 12-12s12 4 12 12z"/></g></svg>Management<br><span style="margin-left:-42px">Development</span></h4>
    <p>Lorsem habitasse platea dictumst. Aliquam in est leo. Aliquam ut urna pulvinar ipsum ultricies fringilla et sed magna. Duis faucibus</p>
    <a class="btn" href="#">know more...</a>
  </article>

  <h2 class="section-title heading" style="top:764px"><span>Our <em>Clients &amp; Partners List</em></span></h2>

  <div class="client" style="left:56px"><i></i>Northmark</div>
  <div class="client" style="left:290px"><i></i>Harbor Ledger</div>
  <div class="client" style="left:574px"><i></i>Relay Wire</div>
  <div class="client" style="left:818px"><i></i>Quillfield</div>
</main>
</body>
</html>
```